Brightwell Pictures Business Card

Hello,

i would like to have a dynamic, creative but tasteful card, colour used, front and back. I have attached a sample card that I liked very much from another individual to give you an idea of the theme/approach, but not colour. Ideally the graphic elements of the Brightwell Logo are brought into the design.

Target Market(s)

North America

Industry/Entity Type

Film Production

Contact Information for Business Card

Mirela Vantasch
President/Founder
Brightwell Pictures Inc.
587 914 3362
mirela@brightwellpix.tv

Font styles to use
Sans Serif

Colors
6b449b
5c5c5c
fdfdfd
000000

Requirements
Must have
• Logo, name, Company name, email and cell number. no Address line to be included.
Should not have
• any unrelated GFX elements, serif fonts

```html
<!DOCTYPE html>
<html lang="en">
<head>
<meta charset="utf-8">
<title>Brightwell Pictures Business Card</title>
<link rel="stylesheet" href="https://fonts.googleapis.com/css2?family=Roboto:wght@400;500;700;900&display=swap">
<style>
  :root {
    --purple: #6b449b;
    --purple-bright: #7a4fc0;
    --grey: #5c5c5c;
    --grey-light: #a9a9ae;
    --white: #fdfdfd;
    --black: #000000;
    --card-black: #0b0b0c;
    --stage: #2a2a2d;
  }
  * { margin: 0; padding: 0; box-sizing: border-box; }
  html, body {
    width: 1200px; height: 900px; overflow: hidden;
    background: var(--stage);
    font-family: "Roboto", sans-serif;
  }
  .stage { position: relative; width: 1200px; height: 900px; }
  .card {
    position: absolute;
    width: 620px; height: 354px;
    left: 290px;
    overflow: hidden;
    box-shadow: 0 14px 40px rgba(0,0,0,.55);
  }
  .card--front { top: 476px; background: var(--card-black); }
  .card--back { top: 70px; background: var(--purple); }

  .wordmark {
    display: flex; align-items: center; gap: 12px;
    font-weight: 900; color: var(--grey-light);
    letter-spacing: -0.5px; white-space: nowrap;
  }
  .wordmark__dot {
    width: 18px; height: 18px; border-radius: 50%;
    background: var(--purple-bright); flex: none;
  }

  .card--front .wordmark { position: absolute; left: 40px; top: 150px; font-size: 34px; }
  .divider {
    position: absolute; left: 372px; top: 92px;
    width: 2px; height: 170px; background: var(--grey);
  }
  .contact-block { position: absolute; }
  .card--front .contact-block { left: 398px; top: 96px; }

  .person__name {
    font-weight: 700; font-size: 27px; color: var(--purple-bright);
    line-height: 1.1; white-space: nowrap;
  }
  .person__title {
    display: inline-block;
    font-size: 15px; color: var(--grey-light);
    padding: 3px 0 5px; margin-bottom: 14px;
    border-bottom: 1px solid var(--grey-light);
  }
  .contact-list { list-style: none; }
  .contact-list li {
    display: flex; align-items: center; gap: 10px;
    font-size: 17px; font-weight: 500; color: var(--white);
    margin-bottom: 8px; white-space: nowrap;
  }
  .contact-icon {
    width: 20px; height: 20px; background: var(--purple-bright);
    display: flex; align-items: center; justify-content: center; flex: none;
  }

  .back-shape { position: absolute; inset: 0; }
  .card--back .contact-block { left: 150px; top: 84px; }
  .card--back .person__name { font-size: 26px; }
  .card--back .person__title { font-size: 14px; margin-bottom: 12px; }
  .card--back .contact-list li { font-size: 15px; margin-bottom: 7px; }
  .card--back .wordmark { position: absolute; left: 130px; top: 236px; font-size: 34px; }
</style>
</head>
<body>
<main class="stage">

  <section class="card card--back" aria-label="Business card back">
    <svg class="back-shape" width="620" height="354" viewBox="0 0 620 354">
      <ellipse cx="250" cy="420" rx="378" ry="398" fill="#8c8c90" role="img" aria-label="Grey textured band following the curve"/>
      <ellipse cx="250" cy="420" rx="360" ry="380" fill="#0b0b0c"/>
    </svg>
    <div class="contact-block">
      <div class="person__name">Mirela Vantasch</div>
      <div class="person__title">President/Founder</div>
      <ul class="contact-list">
        <li><span class="contact-icon"><svg width="12" height="12" viewBox="0 0 24 24"><path fill="#fdfdfd" d="M6.6 10.8a15 15 0 0 0 6.6 6.6l2.2-2.2c.3-.3.7-.4 1-.2 1.1.4 2.3.6 3.6.6.6 0 1 .4 1 1V20c0 .6-.4 1-1 1A17 17 0 0 1 3 4c0-.6.4-1 1-1h3.5c.6 0 1 .4 1 1 0 1.3.2 2.5.6 3.6.1.3 0 .7-.2 1z"/></svg></span>587 914 3362</li>
        <li><span class="contact-icon"><svg width="12" height="12" viewBox="0 0 24 24"><path fill="none" stroke="#fdfdfd" stroke-width="2.4" d="M3 5h18v14H3zM3 5l9 8 9-8"/></svg></span>mirela@brightwellpix.tv</li>
      </ul>
    </div>
    <div class="wordmark"><span class="wordmark__dot"></span>Brightwell Pictures</div>
  </section>

  <section class="card card--front" aria-label="Business card front">
    <div class="wordmark"><span class="wordmark__dot"></span>Brightwell Pictures</div>
    <div class="divider"></div>
    <div class="contact-block">
      <div class="person__name">Mirela Vantasch</div>
      <div class="person__title">President/Founder</div>
      <ul class="contact-list">
        <li><span class="contact-icon"><svg width="12" height="12" viewBox="0 0 24 24"><path fill="#fdfdfd" d="M6.6 10.8a15 15 0 0 0 6.6 6.6l2.2-2.2c.3-.3.7-.4 1-.2 1.1.4 2.3.6 3.6.6.6 0 1 .4 1 1V20c0 .6-.4 1-1 1A17 17 0 0 1 3 4c0-.6.4-1 1-1h3.5c.6 0 1 .4 1 1 0 1.3.2 2.5.6 3.6.1.3 0 .7-.2 1z"/></svg></span>587 914 3362</li>
        <li><span class="contact-icon"><svg width="12" height="12" viewBox="0 0 24 24"><path fill="none" stroke="#fdfdfd" stroke-width="2.4" d="M3 5h18v14H3zM3 5l9 8 9-8"/></svg></span>mirela@brightwellpix.tv</li>
      </ul>
    </div>
  </section>

</main>
</body>
</html>
```